Business Cards + Flyer + Letterhead for Care Recruitment Agency

We are a recruitment agency for the health & care sector. We need designs made for business cards, A5 double-sided flyer, and a letterhead template.

Our branding message is professionalism, care, compassion, expertise. We are experts in recruitment for the care & health industry.

Our logo source files and colours are here - https://www.filevault-example.net/sh/qplr82nvzkx/BBKdLm4ORTe93pWqHnZxYa?dl=0

For the business card, I have attached an example we like. We want a vertical business card design, something very similar to the example given. The design should match our logo in terms of brand colors. On one side should be our logo, our website (www.penhollowbrook.co.uk) and Care Recruitment Specialists written somewhere visible that fits, between our logo and the website at the bottom. On the other side should be our details.

Details on the front:

Logo with slogan
Care Recruitment Specialists
www.penhollowbrook.co.uk

Details on the back:

Marcus Ellory
Managing Director

Rowan Court, 41-47 Tillwick St, Birmingham, B9 7QX
07612 459073
marcus@penhollowbrook.co.uk
www.penhollowbrook.co.uk

Deirdre Penhollow
Business Development Director

07831 204968
deirdre@penhollowbrook.co.uk
www.penhollowbrook.co.uk

For the A5 flyer, I have attached some pictures we've used for the website, which could be used for the flyer as well. To get a better idea of our branding, please visit our website - https://penhollowbrook.co.uk/

The text for the flyer is also attached.

Finally, the letterhead template should be a docx template with our logo and our identifiable branding (the same shapes and matching colours you will come up with for the business cards and flyer).

```html
<!DOCTYPE html>
<html lang="en">
<head>
<meta charset="utf-8">
<title>Penhollow Brook – Business Cards and Letterhead</title>
<link rel="stylesheet" href="https://fonts.googleapis.com/css2?family=Oswald:wght@300;400&family=Open+Sans:wght@400;600;700&display=swap">
<style>
  :root {
    --backdrop: #e4e5e7;
    --paper: #ffffff;
    --navy: #0b4a72;
    --bright-blue: #2a9fd8;
    --light-blue: #a9d4f0;
    --charcoal: #1e232c;
    --ink: #3b3f45;
    --muted-ink: #5a5f66;
    --pale-text: #d8e6f1;
    --signature-tone: #e9edf1;
  }
  * { box-sizing: border-box; margin: 0; padding: 0; }
  html, body { width: 1200px; height: 1125px; overflow: hidden; }
  body {
    background: var(--backdrop);
    position: relative;
    font-family: "Open Sans", Arial, sans-serif;
    color: var(--ink);
  }

  /* ---------- Brand name block ---------- */
  .brand { display: flex; flex-direction: column; align-items: center; gap: 6px; }
  .brand-dot { width: 34px; height: 34px; border-radius: 50%; background: var(--bright-blue); }
  .brand-name {
    font-family: "Open Sans", Arial, sans-serif;
    font-weight: 700; font-size: 12px; letter-spacing: 0.5px;
    color: var(--navy); white-space: nowrap;
  }

  /* ---------- Letterhead ---------- */
  .letterhead {
    position: absolute; left: 488px; top: 85px;
    width: 624px; height: 875px;
    background: var(--paper); overflow: hidden;
  }
  .letterhead .brand { position: absolute; left: 86px; top: 30px; width: 120px; }
  .letterhead .brand-dot { width: 46px; height: 46px; }
  .letterhead .brand-name { font-size: 14px; }

  .letter-contacts {
    position: absolute; right: 80px; top: 54px;
    list-style: none; text-align: right;
    font-size: 11px; line-height: 17.5px; color: var(--muted-ink);
  }
  .letter-contacts li { display: flex; justify-content: flex-end; align-items: center; gap: 7px; }
  .contact-icon { width: 8px; height: 8px; flex: none; }

  .letter-rule {
    position: absolute; left: 87px; top: 153px; width: 456px; height: 2px;
    background: var(--light-blue);
  }
  .letter-date { position: absolute; right: 81px; top: 180px; font-size: 10.5px; color: var(--muted-ink); }
  .letter-greeting { position: absolute; left: 88px; top: 204px; font-size: 15px; color: var(--ink); }
  .letter-body {
    position: absolute; left: 88px; top: 250px; width: 443px;
    font-size: 11px; line-height: 20.6px; text-align: justify; color: var(--muted-ink);
  }
  .letter-body p + p { margin-top: 0; }
  .letter-closing { position: absolute; left: 88px; top: 624px; font-size: 14px; color: var(--ink); }
  .signature-area {
    position: absolute; left: 104px; top: 648px; width: 232px; height: 52px;
    background: var(--signature-tone); border-radius: 4px;
  }
  .signatory-name { position: absolute; left: 88px; top: 718px; font-size: 16px; color: var(--ink); }
  .signatory-role { position: absolute; left: 88px; top: 744px; font-size: 10.5px; color: var(--muted-ink); }
  .letter-waves { position: absolute; left: 0; bottom: 0; width: 624px; height: 130px; display: block; }

  /* ---------- Business cards ---------- */
  .business-card {
    position: absolute; top: 330px; width: 269px; height: 392px;
    background: var(--paper); overflow: hidden;
  }
  .card-front { left: 97px; }
  .card-back { left: 375px; }
  .card-waves { position: absolute; inset: 0; width: 269px; height: 392px; display: block; }
  .business-card .brand { position: absolute; left: 0; right: 0; top: 76px; }

  .card-headline {
    position: absolute; left: 0; right: 0; top: 162px; text-align: center;
    font-family: "Oswald", "Arial Narrow", sans-serif; font-weight: 300;
    font-size: 22px; line-height: 28px; color: var(--navy);
  }
  .card-subline {
    position: absolute; left: 0; right: 0; top: 194px; text-align: center;
    font-family: "Oswald", "Arial Narrow", sans-serif; font-weight: 300;
    font-size: 15px; letter-spacing: 1.6px; color: var(--navy);
  }
  .card-back .card-subline {
    font-family: "Open Sans", Arial, sans-serif; font-weight: 400;
    font-size: 12.5px; letter-spacing: 0; top: 196px;
  }
  .card-website {
    position: absolute; left: 0; right: 0; top: 359px; text-align: center;
    font-size: 10.5px; letter-spacing: 0.4px; color: var(--light-blue);
  }
  .card-contacts {
    position: absolute; right: 8px; top: 296px; list-style: none;
    font-size: 9px; line-height: 16.5px; color: var(--pale-text); text-align: right;
  }
  .card-contacts li { display: flex; justify-content: flex-end; align-items: center; gap: 8px; }
  .card-contacts .contact-icon { width: 7px; height: 7px; }
  .icon-spacer { width: 7px; flex: none; }
</style>
</head>
<body>

  <!-- Letterhead -->
  <article class="letterhead">
    <div class="brand">
      <span class="brand-dot"></span>
      <span class="brand-name">PENHOLLOW BROOK</span>
    </div>

    <ul class="letter-contacts">
      <li>Rowan Court
        <svg class="contact-icon" viewBox="0 0 8 8"><path d="M4 0a3 3 0 0 1 3 3c0 2-3 5-3 5S1 5 1 3a3 3 0 0 1 3-3z" fill="#2a9fd8"/></svg>
      </li>
      <li>41-47 Tillwick St, Birmingham, B9 7QX <span class="contact-icon"></span></li>
      <li>deirdre@penhollowbrook.co.uk
        <svg class="contact-icon" viewBox="0 0 8 8"><rect x="0" y="1.5" width="8" height="5" fill="#2a9fd8"/></svg>
      </li>
      <li>www.penhollowbrook.co.uk
        <svg class="contact-icon" viewBox="0 0 8 8"><circle cx="4" cy="4" r="4" fill="#2a9fd8"/></svg>
      </li>
    </ul>

    <div class="letter-rule"></div>
    <p class="letter-date">Friday, 01/01/2020</p>
    <p class="letter-greeting">Dear customer</p>

    <div class="letter-body">
      <p>Lorem ipsum dolor sit amet, consectetur adipiscing elit, set eiusmod tempor incidunt et labore et dolore magna aliquam. Ut enim ad minim veniam, quis nostrud exerc. Irure dolor in reprehend incididunt ut labore et dolore magna aliqua. Ut enim ad minim veniam is nostrud exercitation ullam mmodo consequet. Duis aute in voluptate velit esse cillum dolore eu fugiat nulla pariatur. At vero eos et accusam dignissum qui blandit est praesent. Trenz pruca beynocguon doas nog ba useing phen roxas. Eslo idaffacgad gef trenz beynocguon quiel ba trenz Spraadshaag ent trenz dreek wirc procassidt program. Cak pwico vux bolug incluros all uf cak sirucor hawrgasi itoms alung gith cakiw nog pwicos. Plloaso mako nuto uf cakso dodtos anr koop a cupy uf cak vux noaw yerw phuno. Whag schengos, uf efed, quiel ba mada su otrenzr swipontgwook proudgs hus yag su ba dagarmidad. Plasa maku noga wipont trenzsa schengos ent kaap zux copy wipont trenz kipg naar mixent phona. Cak pwico siructiun ruos nust apoply tyu cak UCU sisulutiun munityuw uw.</p>
      <p>Sincerely yours,</p>
    </div>

    <p class="letter-closing">Your Sincerely</p>
    <div class="signature-area" role="img" aria-label="Handwritten signature of Marcus Ellory"></div>
    <p class="signatory-name">Marcus Ellory</p>
    <p class="signatory-role">Managing Director</p>

    <svg class="letter-waves" viewBox="0 0 624 130" preserveAspectRatio="none" aria-hidden="true">
      <path d="M0 58 C160 8 360 18 624 44 V130 H0 Z" fill="var(--light-blue)"/>
      <path d="M0 66 C170 22 370 32 624 60 V130 H0 Z" fill="var(--bright-blue)"/>
      <path d="M0 74 C180 36 390 54 624 76 V130 H0 Z" fill="var(--navy)"/>
    </svg>
  </article>

  <!-- Business card: front -->
  <section class="business-card card-front">
    <svg class="card-waves" viewBox="0 0 269 392" aria-hidden="true">
      <path d="M0 0 H269 V24 C200 12 120 40 0 26 Z" fill="var(--light-blue)"/>
      <path d="M0 0 H269 V14 C200 4 120 30 0 14 Z" fill="var(--navy)"/>
      <path d="M0 262 C80 214 170 226 269 190 V392 H0 Z" fill="var(--light-blue)"/>
      <path d="M0 272 C90 234 180 244 269 212 V392 H0 Z" fill="var(--navy)"/>
      <path d="M0 300 C90 270 180 296 269 262 V276 C180 308 90 284 0 312 Z" fill="var(--bright-blue)"/>
      <path d="M0 330 C90 312 180 334 269 300 V392 H0 Z" fill="var(--charcoal)"/>
    </svg>
    <div class="brand">
      <span class="brand-dot"></span>
      <span class="brand-name">PENHOLLOW BROOK</span>
    </div>
    <h2 class="card-headline">Care Recruitment</h2>
    <p class="card-subline">Specialists</p>
    <p class="card-website">www.penhollowbrook.co.uk</p>
  </section>

  <!-- Business card: back -->
  <section class="business-card card-back">
    <svg class="card-waves" viewBox="0 0 269 392" aria-hidden="true">
      <path d="M0 0 H269 V24 C200 12 120 40 0 26 Z" fill="var(--light-blue)"/>
      <path d="M0 0 H269 V14 C200 4 120 30 0 14 Z" fill="var(--navy)"/>
      <path d="M0 232 C80 196 170 212 269 192 V392 H0 Z" fill="var(--light-blue)"/>
      <path d="M0 242 C90 210 180 226 269 206 V392 H0 Z" fill="var(--navy)"/>
      <path d="M0 262 C90 236 180 262 269 236 V250 C180 276 90 250 0 276 Z" fill="var(--bright-blue)"/>
      <path d="M0 284 C90 266 180 288 269 262 V392 H0 Z" fill="var(--charcoal)"/>
    </svg>
    <div class="brand">
      <span class="brand-dot"></span>
      <span class="brand-name">PENHOLLOW BROOK</span>
    </div>
    <h2 class="card-headline">Marcus Ellory</h2>
    <p class="card-subline">Managing Director</p>
    <ul class="card-contacts">
      <li>marcus@penhollowbrook.co.uk
        <svg class="contact-icon" viewBox="0 0 8 8"><rect x="0" y="1.5" width="8" height="5" fill="#2a9fd8"/></svg>
      </li>
      <li>www.penhollowbrook.co.uk
        <svg class="contact-icon" viewBox="0 0 8 8"><circle cx="4" cy="4" r="4" fill="#2a9fd8"/></svg>
      </li>
      <li>Rowan Court <span class="icon-spacer"></span></li>
      <li>41-47 Tillwick St, Birmingham, B9 7QX <span class="icon-spacer"></span></li>
      <li>07612 459073
        <svg class="contact-icon" viewBox="0 0 8 8"><path d="M4 0a3 3 0 0 1 3 3c0 2-3 5-3 5S1 5 1 3a3 3 0 0 1 3-3z" fill="#2a9fd8"/></svg>
      </li>
    </ul>
  </section>

</body>
</html>
```